Editable PDF and PowerPoint template /form

We need a fully editable form/template in PDF and PowerPoint. I have done a mock up with detailed instructions but happy to provide more detail. This is going to be used in our strategic planning monitoring for partner companies that we manage. The editable text boxes get bigger and smaller depending on the content we put in there. People also need to be able to drop their logo into the documents easily.

```html
<!DOCTYPE html>
<html lang="en">
<head>
<meta charset="utf-8">
<title>Strategic Initiative Progress Tracker</title>
<link href="https://fonts.googleapis.com/css2?family=Roboto:wght@400;500&display=swap" rel="stylesheet">
<style>
  :root {
    --ink: #3f3f3f;
    --field-bg: #ebf8f3;
    --field-line: #cfe6dd;
    --head-bg: #fdf3e8;
    --row-alt: #fef5ea;
    --grid-line: #e2d6cc;
    --swoosh-light: #f2f2f2;
    --swoosh-dark: #a9a9a9;
    --footer-band: #f5f5f5;
    --key-badge: #c4c4c4;
    --blue: #1ec0ec;
    --red: #e8141b;
    --amber: #f57a10;
    --green: #0e9f3c;
  }
  * { box-sizing: border-box; margin: 0; padding: 0; }
  html, body { width: 1200px; height: 848px; overflow: hidden; background: #fff; }
  body { font-family: "Roboto", Arial, sans-serif; color: var(--ink); position: relative; }

  .top-swoosh { position: absolute; top: 0; left: 0; width: 1200px; height: 70px; }

  .details { position: absolute; top: 79px; left: 44px; display: flex; gap: 10px; }
  .details__field {
    height: 48px; background: var(--field-bg); border: 1px solid var(--field-line);
    font-size: 16px; font-weight: 500; display: flex; align-items: center; padding-left: 16px;
  }
  .details__field--business { width: 442px; }
  .details__field--owner { width: 442px; }
  .details__field--date { width: 209px; margin-left: -1px; }
  .date-slash { margin-left: 36px; }
  .date-slash + .date-slash { margin-left: 40px; }

  .tracker {
    position: absolute; top: 143px; left: 45px; width: 1109px;
    border-collapse: collapse; table-layout: fixed;
  }
  .tracker th, .tracker td { border: 1px solid var(--grid-line); }
  .tracker th {
    height: 59px; background: var(--head-bg); font-size: 16px; font-weight: 500;
    text-align: left; line-height: 1.1; padding-left: 16px;
  }
  .tracker th.tracker__centered { text-align: center; padding-left: 0; }
  .tracker td { height: 46px; }
  .tracker tbody tr:nth-child(even) td { background: var(--row-alt); }

  .footer-band { position: absolute; left: 0; top: 800px; width: 1200px; height: 48px; background: var(--footer-band); }
  .brag-key {
    position: absolute; top: 786px; left: 32px; width: 1136px; height: 37px;
    background: #fff; border: 1px solid #dcdcdc; border-radius: 19px;
    display: flex; align-items: center; font-size: 11.2px; white-space: nowrap;
  }
  .brag-key__badge {
    width: 52px; height: 37px; margin: -1px 0 0 -1px; border-radius: 19px 0 0 19px;
    background: var(--key-badge); font-size: 12px; font-weight: 500; line-height: 1;
    display: flex; align-items: center; justify-content: center; text-align: center; color: #333;
  }
  .brag-key__item { display: flex; align-items: center; margin-left: 12px; }
  .brag-key__item::before { content: ""; width: 10px; height: 10px; margin-right: 6px; background: currentColor; }
  .brag-key__item--blue { color: var(--blue); margin-left: 14px; }
  .brag-key__item--red { color: var(--red); }
  .brag-key__item--amber { color: var(--amber); }
  .brag-key__item--green { color: var(--green); }
</style>
</head>
<body>
  <svg class="top-swoosh" viewBox="0 0 1200 70" aria-hidden="true">
    <path d="M0 0 H1200 V40 C1050 55 950 48 800 28 C560 0 300 30 0 50 Z" fill="var(--swoosh-light)"/>
    <path d="M0 42 C250 52 500 20 800 28 C950 34 1050 60 1200 48 V60 C1050 66 930 56 800 36 C500 28 250 58 0 50 Z" fill="#d9d9d9"/>
    <path d="M800 30 C950 40 1060 62 1200 44 V62 C1060 68 940 56 800 34 Z" fill="var(--swoosh-dark)"/>
  </svg>

  <div class="details">
    <div class="details__field details__field--business">Business Name:</div>
    <div class="details__field details__field--owner">Owner Name:</div>
    <div class="details__field details__field--date">Date:<span class="date-slash">/</span><span class="date-slash">/</span></div>
  </div>

  <table class="tracker">
    <colgroup>
      <col style="width:292px"><col style="width:117px"><col style="width:116px"><col style="width:292px"><col style="width:292px">
    </colgroup>
    <thead>
      <tr>
        <th>STRATEGIC INITIATIVE/<br>ACTIVITY</th>
        <th class="tracker__centered">TIMELINE</th>
        <th>RAG<br>STATUS</th>
        <th class="tracker__centered">PROGRESS COMMENTARY</th>
        <th style="padding-left:38px">IF AMBER/RED MITIGATION<br>REQUIRED</th>
      </tr>
    </thead>
    <tbody>
      <tr><td></td><td></td><td></td><td></td><td></td></tr>
      <tr><td></td><td></td><td></td><td></td><td></td></tr>
      <tr><td></td><td></td><td></td><td></td><td></td></tr>
      <tr><td></td><td></td><td></td><td></td><td></td></tr>
      <tr><td></td><td></td><td></td><td></td><td></td></tr>
      <tr><td></td><td></td><td></td><td></td><td></td></tr>
      <tr><td></td><td></td><td></td><td></td><td></td></tr>
      <tr><td></td><td></td><td></td><td></td><td></td></tr>
      <tr><td></td><td></td><td></td><td></td><td></td></tr>
      <tr><td></td><td></td><td></td><td></td><td></td></tr>
      <tr><td></td><td></td><td></td><td></td><td></td></tr>
      <tr><td></td><td></td><td></td><td></td><td></td></tr>
    </tbody>
  </table>

  <div class="footer-band"></div>
  <div class="brag-key">
    <div class="brag-key__badge">BRAG<br>KEY</div>
    <span class="brag-key__item brag-key__item--blue">BLUE=ACTIVITY COMPLETE</span>
    <span class="brag-key__item brag-key__item--red">RED=NOT ON TRACK, NEED SIGNIFICANT MITIGATION</span>
    <span class="brag-key__item brag-key__item--amber">AMBER=ON TRACK BUT FLAGGING MAY NEED FUTURE MITIGATION</span>
    <span class="brag-key__item brag-key__item--green">GREEN= ON TRACK AND NO ISSUES</span>
  </div>
</body>
</html>
```